Small 3.5x7.5 Book Flyer Need some Design Work

I have the concept and the pictures just need some flair to make it look good.

Basically we want to advertise our product is the same as the dealer product for a much less price. ITs the same thing. maybe says ELIMINATE THE MIDDLEMAN or SAVE MONEY BUYING DIRECT. The BRANDS we sell are DORNSHAWLEY , BRAKU , NOLAQ , PARVIN, HENDARO. The types of machines we sell parts for are ARTICULATED TRUCKS, RIGID FRAME TRUCKS (Those two can be grouped together ARTICULATED/RIGID if room is needed), WHEEL LOADERS, COMPACTORS, SCRAPERS. The types of products we sell are TRANSMISSIONS, DIFFERENTIALS, FINAL DRIVES, BRAKES, CYLINDERS, and NEW PARTS. This should be somewhere to read on their, dont care wear but looks nice.

This needs to be 3.5" (Width) 7.5 " Height. See deign concept. INcluded log and picture of the part to feature.

Target Market(s)

Rock Quarries, Aggregate PRoducers, Construction companies

Industry/Entity Type

Product

Font styles to use
Sans Serif

Colors
ffffff
000000
fbed22

Requirements
Must have
• The bottom should have our logo and phone number 555-017-3248, website http://www.drobtrade.com (you can also see brenvoxtrailco.com for an understanding of what we sell and more pictures). Address: 718 Pellham Row Tressick ND 58317
Nice to have
• I put OURS and THEIRS, but I think now it should be OURS - FACTORY
• And maybe shows that both components include:
• NEW OEM SEALS
• NEW OEM GASKETS
• NEW OEM BEARINGS
• NEW OEM FRICTIONS
• NEW OEM PLATES
• NEW OEM SOLENOIDS
• REBUILT / BALANCED TORQUE CONVERTER
• It would show these things on the side maybe, on both transmissions - basically showing that ours is exactly the same as the factories but a fraction of the cost.
• Maybe we dont need the price tag. Just show all of those things the same and the bottom line after torque converter would be the PRICE in different color so it stands out.

```html
<!DOCTYPE html>
<html lang="en">
<head>
<meta charset="utf-8">
<title>Drobline Industrial Sales – Rack Card</title>
<link rel="stylesheet" href="https://fonts.googleapis.com/css2?family=Bebas+Neue&family=Open+Sans:wght@400;600;800&display=swap">
<style>
  :root {
    --backdrop: #5e5e5e;
    --paper: #ffffff;
    --concrete-light: #ececec;
    --concrete-dark: #d2d2d2;
    --accent: #fbbf1c;
    --ink: #1a1a1a;
    --ink-soft: #2b2b2b;
    --footer: #4a4a4a;
    --metal-light: #dcdcdc;
    --metal-mid: #a9a9a6;
    --metal-dark: #6d6a63;
  }
  * { box-sizing: border-box; margin: 0; padding: 0; }
  html, body {
    width: 704px; height: 1200px; overflow: hidden;
    background: var(--backdrop);
  }
  .rack-card {
    position: absolute; left: 72px; top: 0;
    width: 560px; height: 1200px; overflow: hidden;
    background: linear-gradient(180deg, var(--concrete-light) 0%, var(--concrete-dark) 55%, var(--concrete-light) 100%);
    font-family: "Open Sans", Arial, sans-serif;
    color: var(--ink);
  }
  .swoosh { position: absolute; left: 0; top: 0; width: 560px; height: 1200px; }

  .brand-mark {
    position: absolute; top: 44px; left: 0; width: 560px;
    display: flex; align-items: center; justify-content: center; gap: 14px;
  }
  .brand-mark__dot {
    width: 70px; height: 70px; border-radius: 50%; background: var(--ink);
  }
  .brand-mark__name {
    font-family: "Open Sans", Arial, sans-serif; font-weight: 800;
    font-size: 30px; line-height: 1.05; color: var(--ink); letter-spacing: 1px;
  }
  .headline {
    position: absolute; top: 150px; left: 0; width: 560px; text-align: center;
    font-family: "Bebas Neue", Impact, sans-serif; font-size: 54px; line-height: 1;
    color: var(--accent); letter-spacing: 0.5px;
  }

  .product-photo {
    position: absolute; left: 40px; top: 252px; width: 494px; height: 445px;
    background:
      radial-gradient(ellipse 38% 30% at 66% 32%, var(--metal-light), var(--metal-mid) 60%, transparent 100%),
      radial-gradient(ellipse 40% 32% at 40% 62%, var(--metal-light), var(--metal-mid) 55%, var(--metal-dark) 80%, transparent 100%);
  }
  .price-tag {
    position: absolute; width: 80px; height: 40px;
    background: var(--accent); border: 1.5px solid var(--ink);
    border-radius: 4px 12px 12px 4px;
    font-family: "Bebas Neue", Impact, sans-serif; font-size: 20px;
    display: flex; align-items: center; justify-content: center; padding-left: 8px;
  }
  .price-tag::before {
    content: ""; position: absolute; left: 6px; top: 16px;
    width: 6px; height: 6px; border-radius: 50%; background: var(--concrete-light); border: 1px solid var(--ink);
  }
  .price-tag--ours { left: 466px; top: 362px; transform: rotate(20deg); }
  .price-tag--factory { left: 36px; top: 655px; transform: rotate(-20deg); }
  .photo-caption {
    position: absolute; left: 174px; top: 690px;
    font-family: "Bebas Neue", Impact, sans-serif; font-size: 20px; color: var(--ink);
  }

  .offer-list { position: absolute; top: 764px; }
  .offer-list--parts { left: 18px; }
  .offer-list--products { left: 312px; }
  .offer-list__title {
    display: flex; align-items: center; gap: 6px;
    font-family: "Bebas Neue", Impact, sans-serif; font-size: 28px; line-height: 1; color: var(--ink-soft);
  }
  .offer-list__title svg { width: 28px; height: 30px; }
  .offer-list__items { list-style: none; margin-left: 36px; margin-top: 2px; }
  .offer-list__items li {
    font-size: 19px; line-height: 25.5px; color: var(--ink-soft); letter-spacing: -0.2px;
  }
  .offer-list__items li::before { content: "• "; }

  .brand-row {
    position: absolute; top: 978px; left: 14px; width: 532px;
    display: flex; justify-content: space-between; align-items: center;
  }
  .brand-row span {
    font-family: "Bebas Neue", Impact, sans-serif; font-size: 27px; color: var(--ink-soft); letter-spacing: 0.5px;
  }

  .contact {
    position: absolute; top: 1080px; left: 0; width: 560px; text-align: center; color: var(--paper);
  }
  .contact__phone {
    display: inline-flex; align-items: center; gap: 12px;
    font-family: "Bebas Neue", Impact, sans-serif; font-size: 38px; line-height: 1; color: var(--accent); letter-spacing: 1px;
  }
  .contact__phone svg { width: 30px; height: 30px; }
  .contact__line { font-size: 17px; line-height: 24px; }
  .contact__web { margin-top: 8px; }
</style>
</head>
<body>
<main class="rack-card">
  <svg class="swoosh" viewBox="0 0 560 1200" aria-hidden="true">
    <path d="M0,0 H560 V205 Q280,250 0,205 Z" fill="var(--paper)"/>
    <path d="M0,205 Q280,250 560,205 V216 Q280,262 0,226 Z" fill="var(--accent)"/>
    <path d="M0,1040 Q280,1000 560,1030 V1200 H0 Z" fill="var(--accent)"/>
    <path d="M0,1056 Q280,1022 560,1048 V1200 H0 Z" fill="var(--footer)"/>
  </svg>

  <div class="brand-mark">
    <div class="brand-mark__dot"></div>
    <div class="brand-mark__name">DROBLINE<br>INDUSTRIAL SALES</div>
  </div>

  <h1 class="headline">SAVE MONEY BUYING DIRECT!</h1>

  <div class="product-photo" role="img" aria-label="Two identical rebuilt heavy-equipment transmissions with torque converters, ours in front and the factory unit behind"></div>
  <div class="price-tag price-tag--ours">$19,800</div>
  <div class="price-tag price-tag--factory">$35,900</div>
  <p class="photo-caption">OURS - FACTORY</p>

  <section class="offer-list offer-list--parts">
    <h2 class="offer-list__title">
      <svg viewBox="0 0 28 30" aria-hidden="true"><path d="M2,2 L11,15 L2,28 H8 L17,15 L8,2 Z M11,2 L20,15 L11,28 H17 L26,15 L17,2 Z" fill="var(--accent)"/></svg>
      PARTS
    </h2>
    <ul class="offer-list__items">
      <li>ARTICULATED TRUCKS</li>
      <li>RIGID FRAME TRUCKS</li>
      <li>WHEEL LOADERS</li>
      <li>COMPACTORS</li>
      <li>SCRAPERS</li>
    </ul>
  </section>

  <section class="offer-list offer-list--products">
    <h2 class="offer-list__title">
      <svg viewBox="0 0 28 30" aria-hidden="true"><path d="M2,2 L11,15 L2,28 H8 L17,15 L8,2 Z M11,2 L20,15 L11,28 H17 L26,15 L17,2 Z" fill="var(--accent)"/></svg>
      PRODUCTS
    </h2>
    <ul class="offer-list__items">
      <li>TRANSMISSIONS</li>
      <li>DIFFERENTIALS</li>
      <li>FINAL DRIVES</li>
      <li>BRAKES</li>
      <li>CYLINDERS</li>
      <li>NEW PARTS</li>
    </ul>
  </section>

  <div class="brand-row">
    <span>DORNSHAWLEY</span>
    <span>PARVIN</span>
    <span>HENDARO</span>
    <span>NOLAQ</span>
    <span>BRAKU</span>
  </div>

  <footer class="contact">
    <div class="contact__phone">
      <svg viewBox="0 0 30 30" aria-hidden="true">
        <circle cx="15" cy="15" r="13" fill="none" stroke="var(--accent)" stroke-width="2.2"/>
        <path d="M10.5,8.5 l2.4,-0.6 l1.6,3.6 l-1.6,1.2 q1,2.6 3.6,3.8 l1.3,-1.5 l3.5,1.7 l-0.6,2.4 q-5.5,0.8 -9.3,-4.3 q-2.4,-3.4 -0.9,-6.3 Z" fill="var(--accent)"/>
      </svg>
      555-017-3248
    </div>
    <p class="contact__line contact__web">www.drobtrade.com</p>
    <p class="contact__line">718 Pellham Row Tressick ND 58317</p>
  </footer>
</main>
</body>
</html>
```